Website for "Grupo de Tecnicas Renovadas"

We need a new web design for an enterprise dedicated to environment and energy saving engineering, based in Monterrey, Mexico.
They offer consulting services, mainly to enhance building designs, and they are also resellers for several products in the energy saving field.

The final design should be oriented to engineers and architects, and should communicate professionalism, innovation, environment care.

Here is the website of a partner enterprise, which does pretty much the same:

http://www.vientoclaro.example/

Target Market(s)

mainly architects and engineers looking for solutions on energy efficiency building

Industry/Entity Type

Environment

Requirements
Must have
• Entry page must be quite graphical and intuitive, must have a "products listing" and a "projects portfolio".

```html
<!DOCTYPE html>
<html lang="en">
<head>
<meta charset="utf-8">
<title>Grupo de Tecnicas Renovadas</title>
<link rel="stylesheet" href="https://fonts.googleapis.com/css2?family=Yanone+Kaffeesatz:wght@300;400;700&family=Dosis:wght@400;700&family=Open+Sans:wght@400;700&family=Arimo:wght@400;700&display=swap">
<style>
:root{
  --teal:#1397a6;
  --teal-dark:#0f8d9b;
  --orange:#f5751f;
  --blue:#1aa3d6;
  --heading-blue:#1b9bc9;
  --green:#a6ce39;
  --grey-bg:#f2f2f2;
  --grey-line:#dcdcdc;
  --text-dark:#444;
  --text-mid:#555;
  --white:#fff;
  --cond:"Yanone Kaffeesatz", sans-serif;
  --round:"Dosis", sans-serif;
  --sans:"Open Sans", sans-serif;
  --body:"Arimo", Arial, sans-serif;
}
*{margin:0;padding:0;box-sizing:border-box}
html,body{width:1200px;height:2510px;overflow:hidden;background:var(--white)}
body{position:relative;font-family:var(--body);color:var(--text-dark)}
.abs{position:absolute}

/* header */
.top-strip{left:0;top:0;width:1200px;height:8px;background:var(--teal)}
.brand{left:28px;top:40px;display:flex;align-items:center;gap:12px}
.brand-dot{width:40px;height:40px;border-radius:50%;background:var(--teal)}
.brand-name{font-family:var(--cond);font-weight:400;font-size:27px;color:var(--text-mid);line-height:1}
.nav-home{left:388px;top:7px;width:87px;height:98px;background:var(--orange)}
.nav-home::after{content:"";position:absolute;left:36px;bottom:-8px;border:8px solid transparent;border-bottom:0;border-top-color:var(--orange)}
.nav a{position:absolute;top:52px;font-family:var(--cond);font-size:29px;color:var(--teal);text-decoration:none;letter-spacing:.5px;line-height:1}
.nav a.current{color:var(--white)}

/* hero */
.hero{left:0;top:130px;width:1200px;height:513px;background:linear-gradient(100deg,#1c6f9c 0%,#e8d9d4 38%,#c98f80 52%,#2aa0e0 70%,#2ea6ea 100%)}
.hero-title{right:32px;top:224px;text-align:right;font-family:var(--round);color:var(--white);font-size:42px;line-height:50px;font-weight:400}
.hero-title strong{font-family:var(--cond);font-weight:700;font-size:46px;letter-spacing:.5px}
.dots{left:1059px;top:609px;display:flex;gap:16px}
.dots span{width:18px;height:18px;border-radius:50%;background:var(--white)}
.dots span.on{background:var(--green)}

/* features */
.features{left:0;top:643px;width:1200px;height:221px;background:var(--green)}
.feature{position:absolute;top:40px;width:300px;margin-left:-150px;text-align:center}
.feature svg{display:block;margin:0 auto;height:130px}
.feature-label{display:block;margin-top:16px;font-family:var(--cond);font-size:28px;color:var(--white);letter-spacing:.5px;line-height:1}

/* section headings */
.section-title{font-family:var(--cond);font-weight:300;font-size:44px;color:var(--heading-blue);line-height:1}
.pager{left:1128px;top:930px}

/* projects */
.project{top:996px;width:281px;height:276px;border:2px solid var(--blue);background:var(--blue)}
.project-photo{height:196px}
.project-caption{padding:8px 12px;color:var(--white);font-family:var(--sans)}
.project-caption h3{font-size:21px;font-weight:700;line-height:25px}
.project-caption p{font-size:14px;line-height:17px}

/* clients */
.client{top:1440px;height:60px;display:flex;align-items:center;gap:8px;font-family:var(--sans);font-weight:700;font-size:20px;color:#6b7a86;white-space:nowrap}
.client i{width:16px;height:16px;border-radius:50%;background:#b7c2c9;display:block}

/* products */
.products{left:0;top:1572px;width:1200px;height:482px;background:var(--grey-bg);border-top:3px solid var(--grey-line);border-bottom:3px solid var(--grey-line)}
.products-title{left:34px;top:1652px;font-family:var(--cond);font-weight:300;font-size:42px;line-height:44px;color:var(--text-dark)}
.products-text{left:34px;top:1770px;width:350px;font-size:18px;line-height:21px;color:#666}
.btn-more{left:32px;top:1894px;width:168px;height:38px;border-radius:9px;background:var(--text-dark);color:var(--white);font-family:var(--cond);font-size:25px;line-height:38px;text-align:center}
.product{width:302px;height:167px;background:var(--white);border:5px solid var(--grey-line);padding:14px}
.product-img{width:100%;height:100%}

/* footer */
.foot-title{top:2105px;font-family:var(--cond);font-weight:700;font-size:36px;color:var(--text-mid);line-height:1}
.foot-links{top:2158px;list-style:none;font-size:15px;line-height:21.7px;color:#555}
.field{left:412px;width:281px;height:30px;border-radius:7px;background:#dcdcdc;font-size:13px;font-weight:700;color:#555;padding:7px 18px}
.field-msg{top:2235px;height:119px}
.btn-send{left:609px;top:2369px;width:84px;height:30px;border-radius:3px;background:#6d6d6d;color:var(--white);font-size:14px;font-weight:700;text-align:center;line-height:30px}
.socials{left:894px;top:2159px;display:flex;gap:11px}
.socials span{width:34px;height:34px;border-radius:50%;background:#7a7a7a}
.newsletter{left:894px;top:2207px;font-size:13px;line-height:17px;color:#555}
.field-news{left:894px;top:2255px;width:227px;border-radius:15px;font-weight:400;font-size:13px}
.subscribe{left:898px;top:2302px;font-size:13px;font-weight:700;color:#444}
.phone{left:892px;top:2344px;display:flex;align-items:center;gap:12px;font-family:var(--cond);font-weight:300;font-size:36px;color:#555}
.bottom-bar{left:0;top:2431px;width:1200px;height:79px;background:var(--teal-dark)}
.copyright{left:20px;top:2463px;font-size:14px;color:var(--white)}
.bottom-mark{left:1122px;top:2452px;width:42px;height:42px;border-radius:50%;border:5px solid rgba(255,255,255,.75)}
</style>
</head>
<body>

<header>
  <div class="abs top-strip"></div>
  <div class="abs brand"><span class="brand-dot"></span><span class="brand-name">Grupo de Tecnicas Renovadas</span></div>
  <div class="abs nav-home"></div>
  <nav class="nav">
    <a class="current" href="#" style="left:408px">HOME</a>
    <a href="#" style="left:505px">ABOUT US</a>
    <a href="#" style="left:640px">SERVICES</a>
    <a href="#" style="left:763px">PROJECTS</a>
    <a href="#" style="left:890px">PRODUCTS</a>
    <a href="#" style="left:1024px">CONTACT US</a>
  </nav>
</header>

<section>
  <div class="abs hero" role="img" aria-label="Modern building with glass facade and white cantilevered floors against a blue sky"></div>
  <h1 class="abs hero-title">Use of Natural Resources<br>in <strong>CONSERVING ENERGY</strong></h1>
  <div class="abs dots"><span class="on"></span><span></span><span></span><span></span></div>
</section>

<section class="abs features">
  <div class="feature" style="left:110px;top:40px">
    <svg viewBox="0 0 110 130" width="110" fill="#fff">
      <rect x="10" y="55" width="22" height="75"/><rect x="38" y="10" width="30" height="120"/><rect x="74" y="35" width="28" height="95"/>
      <rect x="44" y="20" width="4" height="100" fill="#a6ce39"/><rect x="56" y="20" width="4" height="100" fill="#a6ce39"/>
    </svg>
    <span class="feature-label">INNOVATIVE DESIGNS</span>
  </div>
  <div class="feature" style="left:408px">
    <svg viewBox="0 0 110 130" width="110" fill="#fff">
      <path d="M54 128 V70 C54 50 62 36 80 30 L104 20 C104 50 92 70 60 74 Z"/>
      <path d="M50 128 V84 C50 70 40 60 20 58 L4 56 C6 76 22 90 50 90 Z"/>
      <rect x="20" y="118" width="70" height="10" rx="5"/>
    </svg>
    <span class="feature-label">ENVIRONMENT FRIENDLY</span>
  </div>
  <div class="feature" style="left:715px">
    <svg viewBox="0 0 110 130" width="110" fill="none" stroke="#fff" stroke-width="7">
      <rect x="8" y="6" width="94" height="84" rx="6"/>
      <path d="M8 34 H102 M8 62 H102 M39 6 V90 M71 6 V90"/>
      <path d="M55 92 V118 M30 122 H80" stroke-width="8"/>
    </svg>
    <span class="feature-label">RENEWABLE ENERGY</span>
  </div>
  <div class="feature" style="left:1051px">
    <svg viewBox="0 0 140 130" width="140" fill="#fff">
      <rect x="10" y="80" width="22" height="50"/><rect x="40" y="60" width="22" height="70"/><rect x="70" y="72" width="22" height="58"/><rect x="100" y="44" width="22" height="86"/>
      <path d="M8 70 L50 36 L78 56 L112 18 L104 12 L134 4 L128 34 L120 26 L80 72 L52 52 L16 80 Z"/>
    </svg>
    <span class="feature-label">ENERGY MARKET ANALYSIS</span>
  </div>
</section>

<section>
  <h2 class="abs section-title" style="left:22px;top:912px">OUR PROJECTS</h2>
  <svg class="abs pager" width="40" height="30" viewBox="0 0 40 30" fill="none" stroke="#1b9bc9" stroke-width="3.5"><path d="M14 6 L6 15 L14 24 M26 6 L34 15 L26 24"/></svg>

  <article class="abs project" style="left:20px">
    <div class="project-photo" role="img" aria-label="Curved modern house with balconies and garden" style="background:linear-gradient(160deg,#8ec6e6,#d9cfc0 55%,#4f6a4a)"></div>
    <div class="project-caption"><h3>Proin dictum element</h3><p>Proin dictum elementum velit usce euismod</p></div>
  </article>
  <article class="abs project" style="left:315px">
    <div class="project-photo" role="img" aria-label="Blue glass facade seen through a white lattice roof" style="background:linear-gradient(160deg,#d8e6ef,#2f6fb8 55%,#143e86)"></div>
    <div class="project-caption"><h3>Nertyase riti masertas</h3><p>Artyauhas asety kertya aset aplicabo nerertase faeskes kertyu ersvitae</p></div>
  </article>
  <article class="abs project" style="left:609px">
    <div class="project-photo" role="img" aria-label="White house with pool and tropical garden" style="background:linear-gradient(170deg,#a9d0ee,#eef0ee 45%,#4f8a4c 75%,#5fb7d6)"></div>
    <div class="project-caption"><h3>Et aliquipx eato commodo</h3><p>Consequataute irure dolor inreprehenderit involuptate velit</p></div>
  </article>
  <article class="abs project" style="left:902px">
    <div class="project-photo" role="img" aria-label="Curved glass building roof edge against the sky" style="background:linear-gradient(160deg,#2a4f7a,#8fb8e0 45%,#eef3f8 70%,#7aa9d8)"></div>
    <div class="project-caption"><h3>Aenean nonummy</h3><p>Fusce suscipit varius mi. Cum sociis natoque penatibus et magnis dis</p></div>
  </article>
</section>

<section>
  <h2 class="abs section-title" style="left:22px;top:1348px">CLIENTS LIST</h2>
  <div class="abs client" style="left:40px"><i></i>Aurelia Group</div>
  <div class="abs client" style="left:248px">Brisa Drinks</div>
  <div class="abs client" style="left:432px">Trivento Consulting</div>
  <div class="abs client" style="left:640px"><i></i>Nubeonline</div>
  <div class="abs client" style="left:808px">Selva Day Spa</div>
  <div class="abs client" style="left:990px">Rutafija Solutions</div>
</section>

<section>
  <div class="abs products"></div>
  <h2 class="abs products-title">ENVIRONMENT &amp; ENERGY<br>SAVING PRODUCTS</h2>
  <p class="abs products-text">Sed ut perspiciatis unde omnis iste nas error sit volm accusantium dolmque laudantium, totam rem aperiam, eaque ipsa quae ab lo invtore veritatis et qasi arecto beatae vitae dicta sunt explicabo</p>
  <div class="abs btn-more">MORE PRODUCTS</div>
  <div class="abs product" style="left:504px;top:1633px"><div class="product-img" role="img" aria-label="Solar panels with batteries and inverter kit" style="background:radial-gradient(ellipse at center,#3c5f9a 0%,#9fb1c9 55%,#fff 80%)"></div></div>
  <div class="abs product" style="left:822px;top:1633px"><div class="product-img" role="img" aria-label="White portable air conditioning unit" style="background:radial-gradient(ellipse at center,#e6e8ea 0%,#cfd3d6 35%,#fff 60%)"></div></div>
  <div class="abs product" style="left:504px;top:1817px"><div class="product-img" role="img" aria-label="Group of energy saving compact fluorescent bulbs" style="background:radial-gradient(ellipse at center,#e9eef0 0%,#bcd0d4 40%,#fff 70%)"></div></div>
  <div class="abs product" style="left:822px;top:1817px"><div class="product-img" role="img" aria-label="Two small wind turbines" style="background:radial-gradient(ellipse at center,#d0d3d6 0%,#eceeef 40%,#fff 70%)"></div></div>
</section>

<footer>
  <h3 class="abs foot-title" style="left:25px">NAVIGATION</h3>
  <ul class="abs foot-links" style="left:27px"><li>Home</li><li>About Us</li><li>Services</li><li>Portfolio</li><li>Products</li></ul>
  <ul class="abs foot-links" style="left:142px"><li>Sitemap</li><li>Support</li><li>Terms &amp; Conditions</li><li>Privacy Policy</li></ul>

  <h3 class="abs foot-title" style="left:413px">EMAIL US</h3>
  <div class="abs field" style="top:2161px">full name</div>
  <div class="abs field" style="top:2198px">email address</div>
  <div class="abs field field-msg"></div>
  <div class="abs btn-send">send</div>

  <h3 class="abs foot-title" style="left:892px">CONNECT WITH US</h3>
  <div class="abs socials"><span></span><span></span><span></span><span></span><span></span></div>
  <p class="abs newsletter">subscribe to our monthly newsletter<br>and get the best deals and discounts</p>
  <div class="abs field field-news">enter email address</div>
  <div class="abs subscribe">&#10148;&nbsp;&nbsp;subscribe now</div>
  <div class="abs phone">
    <svg width="32" height="32" viewBox="0 0 32 32" fill="none" stroke="#555" stroke-width="2.5"><circle cx="16" cy="16" r="14"/><path d="M11 8 l3 4 -2 2 c1 3 3 5 6 6 l2 -2 4 3 -2 3 c-7 0 -13 -6 -13 -13 z" fill="#555" stroke-width="1"/></svg>
    0-81-5550214
  </div>

  <div class="abs bottom-bar"></div>
  <p class="abs copyright">© Copyright 2013 Grupo de Tecnicas Renovadas. All Rights Reserved</p>
  <div class="abs bottom-mark"></div>
</footer>

</body>
</html>
```